Book cover for The Season of the Lantern, A Novel

We need a book cover suitable for PRINT (both trade paperback and hardcover).
General design notes: Prominent color. Photo-realistic elements. Sophisticated. Some dark/shadowy areas.
Genres: Literary, Mystery/Thriller/Suspense
Subgenres: Metaphysical, Action & Adventure
Back-cover text: Could a dark agenda be woven into the architecture of China’s most sacred ancient temple? An agenda that only Tobias Wrenfold is seeing? Or is Tobias off his meds again? If the structure were in fact a doomsday device awaiting an astronomical tripwire—could Tobias stop it? Especially if, wound within his own DNA, lay the very same agenda? Tobias is determined to discover the answer, as soon as he concludes a far more pressing matter involving a sixteen-year-old girl with a most intriguing mutation.
This book as been described as "A richly told, diagnosably insane, meandering yet captivating journey through everything good and bad about sex, drugs, and China---plus a wildly improbable tale about saving the world. In short, not to be missed."
The cover MUST INCLUDE:
1. Something that clearly indicates China.
2. Something that suggests the occult, supernatural, metaphysical, or mystical, ideally with a Chinese spin.
3. Something that suggests depravity or sin of some sort, or at least a general sense of edginess. (The main character is a gambler, addict, and womanizer)
4. "The Season of the Lantern"
5. "A novel"
6. "Edmund Carraway Pell"
7. The back cover needs the back-cover text and a space for an endorsement (you can use the endorsement above).
Three possible ideas:
1. A Lanfeng beer bottle broken in a gutter on the right, the book title and author name crowded on the left. with Chinese star charts above.
2. The torso of a beautiful woman who mutates into a seven-headed hydra that has Chinese-style dragon heads, as the centerpoint of the cover. Author above, book cover below, or vice versa.
3. A Chinese Feng Shui compass, half going off the page, or I Ching trigrams, or a Chinese dragon head, or similar, with the book title and author name taking up most of the cover, with not-too-bright Chinese star charts behind.
Anything else you want to try is fine---we would like to see creative ideas!
Colors
Designer to choose colors to be used in the design.
Look and feel

```html
<!DOCTYPE html>
<html lang="en">
<head>
<meta charset="utf-8">
<title>The Season of the Lantern — Cover Spread</title>
<link rel="stylesheet" href="https://fonts.googleapis.com/css2?family=Cinzel:wght@400;500&family=Crimson+Text:wght@400&family=Raleway:wght@300&display=swap">
<style>
  :root {
    --cover-red: #9a1b2b;
    --title-red: #7c1518;
    --spine-gold: #e3b247;
    --sand-light: #f1cf72;
    --sand-mid: #d9a23a;
    --sand-deep: #9c6414;
    --brass-light: #e6c45a;
    --brass-mid: #b88a26;
    --brass-dark: #6f4a10;
    --gold-panel-top: #e9bb4e;
    --gold-panel-bottom: #cf9a2b;
    --paper: #ffffff;
    --ink-dark: #2a1608;
  }
  * { margin: 0; padding: 0; box-sizing: border-box; }
  html, body { width: 1200px; height: 850px; overflow: hidden; background: #ffffff; }
  .spread { position: relative; width: 1200px; height: 850px; overflow: hidden; }

  /* Photo area behind back art, spine and front */
  .photo-area {
    position: absolute; left: 311px; top: 0; width: 889px; height: 850px; display: block;
  }

  /* Back cover */
  .back-panel {
    position: absolute; left: 0; top: 0; width: 311px; height: 850px;
    background: var(--cover-red); color: var(--paper);
    font-family: "Crimson Text", Georgia, serif;
  }
  .back-blurb {
    position: absolute; left: 59px; top: 86px; width: 226px;
    font-size: 15px; line-height: 25.5px;
  }
  .back-divider {
    position: absolute; left: 59px; top: 503px; width: 226px;
    border-top: 2px dotted rgba(255,255,255,0.85);
  }
  .back-endorsement {
    position: absolute; left: 59px; top: 536px; width: 222px;
    font-size: 15px; line-height: 25.5px;
  }
  .barcode-space {
    position: absolute; left: 343px; top: 669px; width: 188px; height: 118px;
    background: var(--paper);
  }

  /* Spine */
  .spine {
    position: absolute; left: 570px; top: 0; width: 62px; height: 850px;
    background: var(--cover-red);
  }
  .spine-text {
    position: absolute; left: 50%; top: 56px;
    transform-origin: 0 0; transform: rotate(90deg) translateY(-50%);
    white-space: nowrap; display: flex; align-items: center; gap: 92px;
  }
  .spine-title {
    font-family: "Cinzel", "Times New Roman", serif; font-size: 32px;
    color: var(--spine-gold); letter-spacing: 0.5px;
  }
  .spine-author {
    font-family: "Cinzel", "Times New Roman", serif; font-size: 18px;
    color: var(--paper); line-height: 1.1; white-space: normal; width: 200px;
    text-align: center;
  }

  /* Front cover */
  .front-title {
    position: absolute; left: 632px; top: 528px; width: 568px;
    text-align: center; color: var(--title-red);
    font-family: "Cinzel", "Times New Roman", serif; font-weight: 400;
  }
  .title-line { display: block; font-size: 74px; line-height: 1; letter-spacing: 1px; }
  .title-of {
    display: flex; align-items: center; justify-content: center; gap: 6px;
    margin: 4px auto 2px; width: 486px; font-size: 17px; letter-spacing: 1px;
  }
  .title-of::before, .title-of::after {
    content: ""; flex: 1; border-top: 1.5px solid var(--title-red);
  }
  .front-subtitle {
    position: absolute; left: 632px; top: 722px; width: 568px; text-align: center;
    font-family: "Raleway", Arial, sans-serif; font-weight: 300;
    font-size: 23px; letter-spacing: 7px; color: var(--paper);
  }
  .front-author {
    position: absolute; left: 632px; top: 780px; width: 568px; text-align: center;
    font-family: "Cinzel", "Times New Roman", serif; font-size: 33px;
    letter-spacing: 0.5px; color: var(--ink-dark);
  }
</style>
</head>
<body>
<div class="spread">
  <svg class="photo-area" viewBox="0 0 889 850" role="img" aria-label="Photograph of a brass Chinese feng shui luopan compass half buried in golden sand, running from the back cover across to the front">
    <defs>
      <linearGradient id="sandField" x1="0" y1="0" x2="0" y2="1">
        <stop offset="0" stop-color="#d9a23a"/>
        <stop offset="0.45" stop-color="#ecc462"/>
        <stop offset="0.7" stop-color="#e5b64e"/>
        <stop offset="1" stop-color="#c99128"/>
      </linearGradient>
      <radialGradient id="brassDisc" cx="0.5" cy="0.5" r="0.5">
        <stop offset="0" stop-color="#e6c45a"/>
        <stop offset="0.3" stop-color="#c99f35"/>
        <stop offset="0.85" stop-color="#a87b1f"/>
        <stop offset="1" stop-color="#6f4a10"/>
      </radialGradient>
    </defs>
    <rect width="889" height="850" fill="url(#sandField)"/>
    <circle cx="407" cy="318" r="378" fill="url(#brassDisc)" stroke="#6f4a10" stroke-width="4"/>
  </svg>

  <section class="back-panel">
    <p class="back-blurb">Could a dark agenda be woven into the architecture of China’s most sacred ancient temple? An agenda that only Tobias Wrenfold is seeing? Or is Tobias off his meds again? If the structure were in fact a doomsday device awaiting an astronomical tripwire—could Tobias stop it? Especially if, wound within his own DNA, lay the very same agenda? Tobias is determined to discover the answer, as soon as he concludes a far more pressing matter involving a sixteen-year-old girl with a most intriguing mutation.</p>
    <div class="back-divider"></div>
    <p class="back-endorsement">This book as been described as "A richly told, diagnosably insane, meandering yet captivating journey through everything good and bad about sex, drugs, and China---plus a wildly improbable tale about saving the world. In short, not to be missed."</p>
  </section>

  <div class="barcode-space"></div>

  <section class="spine">
    <div class="spine-text">
      <span class="spine-title">The Season of the Lantern</span>
      <span class="spine-author">Edmund Carraway Pell</span>
    </div>
  </section>

  <h1 class="front-title">
    <span class="title-line">The Season</span>
    <span class="title-of">of</span>
    <span class="title-line">The Lantern</span>
  </h1>
  <p class="front-subtitle">A NOVEL</p>
  <p class="front-author">Edmund Carraway Pell</p>
</div>
</body>
</html>
```